Stop Clapping - Get A Job (Attention Grabbing Billboard Design)

We wish to design a moving bill-board for jobs as Community Support Workers
On paper adverts - the job adverts reads:
Are you looking for a role with variety
Are you looking to make a difference to people's lives
Find out more about us at www.kestrelpathlimited.co.uk
Kestrel Path Ltd supports young adults with disabilities that may include learning, physical, and mental health, to live in the community as independently as possible. Our main objective is for these young adults to realise their life's desires, goals and aspirations.
Kestrel Path Ltd are looking for energetic individuals with a caring heart, who can combine their own initiatives, bright personality and a sense of humor to be the Support Worker to such young adults. Work is in 12hour shifts around the clock and any day of the week.
Fully paid training shall be provided although previous experience is desirable and an advantage.
Please send us your cv and a covering letter and we shall be happy to get in touch with you asap. Please note if successful applicants will be subject to a full QTR check.
Part-time hours: 60 per week
Job Types: Full-time, Part-time, Permanent
Salary: £9.00-£11.00 per hour
Schedule:
12 hour shift
Day shift
Monday to Friday
Night shift
Weekends
Experience:
Support Environment: 1 year (Preferred)
Location:
Chatham ZX9 2LP (Preferred)
Licence:
BWK Level 2 Health & Social Care (Preferred)
Work remotely:
No
www.kestrelpathlimited.co.uk
support@kestrelpathgroup.co.uk
Telephone: 0800 712 4093
Target Market(s)
jobless people
employed people looking to make a change to social care
community leaders so they can appreciate the efforts we are making to keeping vulnerable people in the community and out of the GVL therefore saving lives and protecting the GVL
Requirements
Must have
- We are looking for an attention grabbing billboard as this shall be on the side of local buses and on a couple of vans

```html
<!DOCTYPE html>
<html lang="en">
<head>
<meta charset="utf-8">
<title>Kestrel Path – Stop Clapping, Get A Job</title>
<link href="https://fonts.googleapis.com/css2?family=Montserrat:wght@400;500;700;800&family=Bebas+Neue&display=swap" rel="stylesheet">
<style>
  :root {
    --blue: #1a82c4;
    --green: #17a96b;
    --ink: #111111;
    --grey: #5f5f5f;
    --white: #ffffff;
    --page: #ffffff;
  }
  * { margin: 0; padding: 0; box-sizing: border-box; }
  html, body { width: 1200px; height: 1000px; overflow: hidden; background: var(--page); }
  .canvas { position: relative; width: 1200px; height: 1000px; }
  .billboard {
    position: absolute; left: 108px; top: 354px; width: 982px; height: 294px;
    background: var(--white); overflow: hidden;
    box-shadow: 0 12px 28px rgba(0,0,0,0.18);
    font-family: "Montserrat", Arial, sans-serif;
  }
  .billboard-shapes { position: absolute; inset: 0; }
  .brand {
    position: absolute; left: 30px; top: 40px; display: flex; align-items: center; gap: 12px;
  }
  .brand-dot { width: 58px; height: 58px; border-radius: 50%; background: var(--blue); }
  .brand-name { font-weight: 700; font-size: 30px; color: var(--blue); letter-spacing: -0.5px; }
  .divider { position: absolute; width: 2px; background: var(--grey); }
  .divider--head { left: 302px; top: 36px; height: 68px; }
  .divider--contact { left: 329px; top: 244px; height: 30px; }
  .headline { position: absolute; left: 347px; top: 22px; }
  .headline-kicker { font-weight: 800; font-size: 26px; color: var(--ink); line-height: 1; letter-spacing: 0.3px; }
  .headline-main { font-family: "Bebas Neue", Impact, sans-serif; font-size: 76px; color: var(--green); line-height: 0.9; letter-spacing: 0.5px; }
  .questions { position: absolute; left: 29px; top: 147px; color: var(--white); }
  .question-lead { font-weight: 500; font-size: 20.5px; letter-spacing: 0.4px; line-height: 1; }
  .question-main { font-family: "Bebas Neue", Impact, sans-serif; font-size: 29px; letter-spacing: 0.6px; line-height: 1; margin-top: 10px; }
  .phone { position: absolute; left: 28px; top: 241px; display: flex; align-items: center; gap: 7px; }
  .icon-badge { display: inline-flex; align-items: center; justify-content: center; border-radius: 50%; background: var(--green); flex: none; }
  .phone .icon-badge { width: 26px; height: 26px; }
  .phone-number { font-weight: 700; font-size: 30px; color: var(--ink); letter-spacing: 0.2px; }
  .contact-list { position: absolute; left: 356px; top: 238px; list-style: none; }
  .contact-list li { display: flex; align-items: center; gap: 5px; font-size: 16px; font-weight: 500; color: var(--ink); height: 23px; }
  .contact-list .icon-badge { width: 17px; height: 17px; }
  .photo {
    position: absolute; left: 689px; top: 1px; width: 292px; height: 292px; border-radius: 50%;
    background: radial-gradient(circle at 60% 35%, #e9ece6 0%, #cfd5cb 45%, #8e9a80 75%, #5d6a4f 100%);
    border: 5px solid var(--white);
  }
</style>
</head>
<body>
<div class="canvas">
  <section class="billboard">
    <svg class="billboard-shapes" width="982" height="294" viewBox="0 0 982 294" aria-hidden="true">
      <rect x="0" y="129" width="700" height="97" fill="var(--blue)"/>
      <circle cx="842" cy="147" r="228" fill="var(--blue)"/>
      <circle cx="830" cy="130" r="195" fill="var(--green)"/>
    </svg>

    <div class="brand">
      <span class="brand-dot"></span>
      <span class="brand-name">Kestrel Path</span>
    </div>
    <span class="divider divider--head"></span>

    <div class="headline">
      <p class="headline-kicker">STOP CLAPPING</p>
      <p class="headline-main">GET A JOB</p>
    </div>

    <div class="questions">
      <p class="question-lead">ARE YOU LOOKING FOR A ROLE WITH VARIETY ?</p>
      <p class="question-main">ARE YOU LOOKING TO MAKE A DIFFERENCE TO PEOPLE'S LIVES ?</p>
    </div>

    <div class="phone">
      <span class="icon-badge">
        <svg width="14" height="14" viewBox="0 0 24 24" aria-hidden="true"><path fill="#fff" d="M6.6 10.8a15.1 15.1 0 0 0 6.6 6.6l2.2-2.2c.3-.3.7-.4 1-.2 1.1.4 2.3.6 3.6.6.6 0 1 .4 1 1V20c0 .6-.4 1-1 1A17 17 0 0 1 3 4c0-.6.4-1 1-1h3.5c.6 0 1 .4 1 1 0 1.3.2 2.5.6 3.6.1.3 0 .7-.2 1z"/></svg>
      </span>
      <span class="phone-number">0800 712 4093</span>
    </div>
    <span class="divider divider--contact"></span>

    <ul class="contact-list">
      <li>
        <span class="icon-badge"><svg width="11" height="11" viewBox="0 0 24 24" aria-hidden="true"><circle cx="12" cy="12" r="9" fill="none" stroke="#fff" stroke-width="2.5"/><path d="M3 12h18M12 3c3 3 3 15 0 18M12 3c-3 3-3 15 0 18" fill="none" stroke="#fff" stroke-width="2"/></svg></span>
        www.kestrelpathlimited.co.uk
      </li>
      <li>
        <span class="icon-badge"><svg width="10" height="10" viewBox="0 0 24 24" aria-hidden="true"><rect x="2" y="5" width="20" height="14" rx="1" fill="#fff"/><path d="M2 6l10 7 10-7" fill="none" stroke="var(--green)" stroke-width="2"/></svg></span>
        support@kestrelpathgroup.co.uk
      </li>
    </ul>

    <div class="photo" role="img" aria-label="Photo of a job interview at a desk with a young man and an older woman in white shirts, plants behind"></div>
  </section>
</div>
</body>
</html>
```